Weight Loss Banner Ad

We need banner ads for our website, www.bluvantaplan.com. We would like to see Banner ads that represent what you think is the most captivating aspect of The Bluvanta Plan. Please review the website.

The banner ad should be something you REALLY want to click on. It needs to include the name and/or logo and the slogan "Gourmet Meals Direct To Your House"

We will want the final ad in multiple sizes but it should use the same image and copy.

Logo is attached, so are images. Feel free to use your own if you think you have a better on

Size (pixels):
468 x 60
392 x 72
234 x 60
125 x 125
120 x 90
120 x 60
88 x 31
120 x 240
120 x 600
160 x 600

Target Market(s)

Fitness Enthusiast looking to lose weight.

Industry/Entity Type

Weight

Font styles to use
Sans Serif

Requirements
Must have
• See Description
Nice to have
• Should be awesome and make you want to buy some food. Also you may want to say something about the price:

i.e. Starting at only $99

```html
<!DOCTYPE html>
<html lang="en">
<head>
<meta charset="utf-8">
<title>The Bluvanta Plan – Banner Set</title>
<link href="https://fonts.googleapis.com/css2?family=Ubuntu:wght@400;500;700&display=swap" rel="stylesheet">
<style>
  :root {
    --stage: #4a2c17;
    --green-light: #9ad13f;
    --green-mid: #7cb82a;
    --green-dark: #5a9316;
    --ink-green: #2c4a08;
    --white: #ffffff;
    --photo-light: #f1efec;
    --photo-mid: #d9d3cc;
    --photo-warm: #c7a892;
    --btn-top: #ffe83a;
    --btn-bottom: #f6b400;
    --btn-ink: #1a1a00;
  }
  * { box-sizing: border-box; margin: 0; padding: 0; }
  html, body { width: 1200px; height: 878px; overflow: hidden; }
  body {
    background: var(--stage);
    font-family: "Ubuntu", Arial, sans-serif;
    position: relative;
  }
  .banner {
    position: absolute;
    overflow: hidden;
    background: linear-gradient(180deg, var(--green-light), var(--green-dark));
    box-shadow: 0 3px 8px rgba(0,0,0,.45);
    color: var(--white);
  }
  .photo {
    background: linear-gradient(160deg, var(--photo-light) 0%, var(--photo-mid) 55%, var(--photo-warm) 100%);
  }
  .logo {
    font-weight: 700;
    line-height: 1;
    letter-spacing: -0.5px;
  }
  .logo-white { color: var(--white); }
  .logo-green { color: var(--green-mid); }
  .headline { font-weight: 700; line-height: 1.02; }
  .subline { font-weight: 500; color: var(--ink-green); line-height: 1.05; }
  .price-only { font-weight: 400; }
  .price { font-weight: 700; }
  .cta {
    display: inline-block;
    background: linear-gradient(180deg, var(--btn-top), var(--btn-bottom));
    color: var(--btn-ink);
    font-weight: 700;
    border-radius: 999px;
    text-align: center;
    box-shadow: 0 2px 3px rgba(0,0,0,.35);
  }
  .white-panel { background: var(--white); }

  /* Skyscraper 160 x 600 */
  .sky-wide { left: 87px; top: 44px; width: 211px; height: 791px; text-align: center; }
  .sky-wide .logo { position: absolute; top: 24px; left: 0; right: 0; font-size: 27px; }
  .sky-wide .photo { position: absolute; top: 88px; left: 0; width: 211px; height: 323px;
    border-bottom-left-radius: 50% 18px; border-bottom-right-radius: 50% 18px; }
  .sky-wide .headline { position: absolute; top: 430px; left: 0; right: 0; font-size: 42px; }
  .sky-wide .subline { position: absolute; top: 521px; left: 0; right: 0; font-size: 33px; }
  .sky-wide .price-only { position: absolute; top: 606px; left: 0; right: 0; font-size: 28px; }
  .sky-wide .price { position: absolute; top: 636px; left: 0; right: 0; font-size: 64px; }
  .sky-wide .cta { position: absolute; top: 737px; left: 19px; width: 173px; height: 40px; line-height: 40px; font-size: 20px; }

  /* Skyscraper 120 x 600 */
  .sky-narrow { left: 318px; top: 44px; width: 158px; height: 791px; text-align: center; }
  .sky-narrow .logo { position: absolute; top: 30px; left: 0; right: 0; font-size: 21px; }
  .sky-narrow .photo { position: absolute; top: 119px; left: 0; width: 158px; height: 360px;
    border-top-left-radius: 50% 14px; border-top-right-radius: 50% 14px; }
  .sky-narrow .headline { position: absolute; top: 495px; left: 0; right: 0; font-size: 32px; }
  .sky-narrow .subline { position: absolute; top: 568px; left: 0; right: 0; font-size: 26px; }
  .sky-narrow .price-only { position: absolute; top: 640px; left: 0; right: 0; font-size: 24px; }
  .sky-narrow .price { position: absolute; top: 665px; left: 0; right: 0; font-size: 54px; }
  .sky-narrow .cta { position: absolute; top: 733px; left: 10px; width: 138px; height: 36px; line-height: 36px; font-size: 17px; }

  /* Leaderboard 468 x 60 */
  .leader { left: 496px; top: 44px; width: 617px; height: 79px; }
  .leader .logo { position: absolute; left: 10px; top: 30px; font-size: 17px; }
  .leader .photo { position: absolute; left: 112px; top: 0; width: 146px; height: 79px; border-radius: 0 40px 40px 0; }
  .leader .headline { position: absolute; left: 265px; top: 12px; width: 200px; text-align: center; font-size: 23px; }
  .leader .subline { position: absolute; left: 265px; top: 44px; width: 200px; text-align: center; font-size: 18px; }
  .leader .offer { position: absolute; left: 479px; top: 0; width: 138px; height: 79px; border-left: 1px solid rgba(255,255,255,.4); text-align: center; }
  .leader .price-only { font-size: 18px; }
  .leader .price { font-size: 34px; }
  .leader .offer-line { position: absolute; top: 4px; left: 0; right: 0; }
  .leader .cta { position: absolute; top: 46px; left: 12px; width: 116px; height: 24px; line-height: 24px; font-size: 14px; }

  /* Banner 392 x 72 */
  .wide { left: 496px; top: 142px; width: 517px; height: 95px; }
  .wide .photo-panel { position: absolute; left: 0; top: 0; width: 160px; height: 95px; border-radius: 0 40px 40px 0; overflow: hidden; }
  .wide .photo { position: absolute; left: 0; top: 0; width: 70px; height: 95px; }
  .wide .logo { position: absolute; left: 72px; top: 30px; width: 84px; font-size: 15px; }
  .wide .headline { position: absolute; left: 162px; top: 10px; width: 196px; text-align: center; font-size: 24px; }
  .wide .subline { position: absolute; left: 162px; top: 38px; width: 196px; text-align: center; font-size: 22px; }
  .wide .offer { position: absolute; left: 372px; top: 0; width: 145px; height: 95px; border-left: 1px solid rgba(255,255,255,.4); text-align: center; }
  .wide .offer-line { position: absolute; top: 6px; left: 0; right: 0; }
  .wide .price-only { font-size: 20px; }
  .wide .price { font-size: 36px; }
  .wide .cta { position: absolute; top: 53px; left: 10px; width: 130px; height: 30px; line-height: 30px; font-size: 16px; }

  /* Half banner 234 x 60 */
  .half { left: 496px; top: 257px; width: 309px; height: 79px; }
  .half .photo { position: absolute; left: 0; top: 0; width: 84px; height: 79px; border-radius: 0 30px 30px 0; }
  .half .headline { position: absolute; left: 92px; top: 3px; width: 210px; text-align: center; font-size: 19px; }
  .half .subline { position: absolute; left: 92px; top: 25px; width: 210px; text-align: center; font-size: 14px; }
  .half .logo { position: absolute; left: 90px; top: 54px; font-size: 14px; }
  .half .offer { position: absolute; left: 212px; top: 42px; width: 95px; text-align: center; }
  .half .price-only { font-size: 14px; }
  .half .price { font-size: 24px; }

  /* Square 125 x 125 */
  .square { left: 496px; top: 356px; width: 165px; height: 165px; }
  .square .photo { position: absolute; left: 0; top: 0; width: 75px; height: 165px; }
  .square .white-panel { position: absolute; left: 75px; top: 0; width: 90px; height: 52px; }
  .square .logo { position: absolute; left: 78px; top: 18px; font-size: 13px; }
  .square .headline { position: absolute; left: 75px; top: 56px; width: 90px; text-align: center; font-size: 18px; }
  .square .subline { position: absolute; left: 75px; top: 100px; width: 90px; text-align: center; font-size: 14px; }

  /* Vertical 120 x 240 */
  .vertical { left: 680px; top: 356px; width: 158px; height: 316px; text-align: center; }
  .vertical .white-panel { position: absolute; left: 0; top: 0; width: 158px; height: 124px; }
  .vertical .photo { position: absolute; left: 0; top: 0; width: 70px; height: 124px; }
  .vertical .logo { position: absolute; left: 72px; top: 40px; width: 84px; font-size: 16px; }
  .vertical .headline { position: absolute; top: 132px; left: 0; right: 0; font-size: 24px; }
  .vertical .subline { position: absolute; top: 188px; left: 0; right: 0; font-size: 19px; }
  .vertical .offer-line { position: absolute; top: 237px; left: 0; right: 0; }
  .vertical .price-only { font-size: 19px; }
  .vertical .price { font-size: 32px; }
  .vertical .cta { position: absolute; top: 280px; left: 20px; width: 118px; height: 26px; line-height: 26px; font-size: 14px; }

  /* Button 120 x 90 */
  .button-ad { left: 496px; top: 541px; width: 158px; height: 119px; }
  .button-ad .white-panel { position: absolute; inset: 0; }
  .button-ad .photo { position: absolute; left: 0; top: 0; width: 66px; height: 119px; }
  .button-ad .logo { position: absolute; left: 68px; top: 12px; font-size: 13px; }
  .button-ad .headline { position: absolute; left: 66px; top: 42px; width: 92px; text-align: center; font-size: 16px; color: var(--green-mid); }
  .button-ad .subline { position: absolute; left: 66px; top: 82px; width: 92px; text-align: center; font-size: 13px; }

  /* Button 120 x 60 */
  .button-small { left: 496px; top: 679px; width: 158px; height: 79px; }
  .button-small .white-panel { position: absolute; inset: 0; }
  .button-small .photo { position: absolute; left: 0; top: 0; width: 58px; height: 79px; }
  .button-small .logo { position: absolute; left: 62px; top: 16px; font-size: 14px; }
  .button-small .cta { position: absolute; left: 102px; top: 50px; width: 46px; height: 20px; line-height: 20px; font-size: 12px; }

  /* Micro bar 88 x 31 */
  .micro { left: 496px; top: 778px; width: 116px; height: 41px; }
  .micro .white-panel { position: absolute; inset: 0; }
  .micro .photo { position: absolute; left: 0; top: 0; width: 32px; height: 41px; }
  .micro .logo { position: absolute; left: 35px; top: 13px; font-size: 11px; }
</style>
</head>
<body>

  <section class="banner sky-wide" aria-label="160 by 600 skyscraper">
    <div class="logo logo-white">The Bluvanta Plan</div>
    <div class="photo" role="img" aria-label="Photo of a woman eating a fresh salad"></div>
    <div class="headline">Gourmet<br>Meals</div>
    <div class="subline">Direct To<br>Your House</div>
    <div class="price-only">only</div>
    <div class="price">$99!</div>
    <span class="cta">START NOW!</span>
  </section>

  <section class="banner sky-narrow" aria-label="120 by 600 skyscraper">
    <div class="logo logo-white">The Bluvanta Plan</div>
    <div class="photo" role="img" aria-label="Photo of a woman eating a fresh salad"></div>
    <div class="headline">Gourmet<br>Meals</div>
    <div class="subline">Direct To<br>Your House</div>
    <div class="price-only">only</div>
    <div class="price">$99!</div>
    <span class="cta">START NOW!</span>
  </section>

  <section class="banner leader" aria-label="468 by 60 leaderboard">
    <div class="logo logo-white">The Bluvanta Plan</div>
    <div class="photo" role="img" aria-label="Photo of a woman eating a fresh salad"></div>
    <div class="headline">Gourmet Meals</div>
    <div class="subline">Direct To Your House</div>
    <div class="offer">
      <div class="offer-line"><span class="price-only">only </span><span class="price">$99!</span></div>
      <span class="cta">START NOW!</span>
    </div>
  </section>

  <section class="banner wide" aria-label="392 by 72 banner">
    <div class="photo-panel white-panel">
      <div class="photo" role="img" aria-label="Photo of a woman eating a fresh salad"></div>
      <div class="logo logo-green">The Bluvanta Plan</div>
    </div>
    <div class="headline">Gourmet Meals</div>
    <div class="subline">Direct To<br>Your House</div>
    <div class="offer">
      <div class="offer-line"><span class="price-only">only </span><span class="price">$99!</span></div>
      <span class="cta">START NOW!</span>
    </div>
  </section>

  <section class="banner half" aria-label="234 by 60 half banner">
    <div class="photo" role="img" aria-label="Photo of a woman eating a fresh salad"></div>
    <div class="headline">Gourmet Meals</div>
    <div class="subline">Direct To Your House</div>
    <div class="logo logo-white">The Bluvanta Plan</div>
    <div class="offer"><span class="price-only">only </span><span class="price">$99!</span></div>
  </section>

  <section class="banner square" aria-label="125 by 125 square">
    <div class="photo" role="img" aria-label="Photo of a woman eating a fresh salad"></div>
    <div class="white-panel"></div>
    <div class="logo logo-green">The Bluvanta Plan</div>
    <div class="headline">Gourmet<br>Meals</div>
    <div class="subline">Direct To<br>Your House</div>
  </section>

  <section class="banner vertical" aria-label="120 by 240 vertical banner">
    <div class="white-panel"></div>
    <div class="photo" role="img" aria-label="Photo of a woman eating a fresh salad"></div>
    <div class="logo logo-green">The Bluvanta Plan</div>
    <div class="headline">Gourmet<br>Meals</div>
    <div class="subline">Direct To<br>Your House</div>
    <div class="offer-line"><span class="price-only">only </span><span class="price">$99!</span></div>
    <span class="cta">START NOW!</span>
  </section>

  <section class="banner button-ad" aria-label="120 by 90 button">
    <div class="white-panel"></div>
    <div class="photo" role="img" aria-label="Photo of a woman eating a fresh salad"></div>
    <div class="logo logo-green">The Bluvanta Plan</div>
    <div class="headline">Gourmet<br>Meals</div>
    <div class="subline">Direct To<br>Your House</div>
  </section>

  <section class="banner button-small" aria-label="120 by 60 button">
    <div class="white-panel"></div>
    <div class="photo" role="img" aria-label="Photo of a woman eating a fresh salad"></div>
    <div class="logo logo-green">The Bluvanta Plan</div>
    <span class="cta">GO
      <svg width="7" height="8" viewBox="0 0 7 8" aria-hidden="true"><path d="M0 0 L7 4 L0 8 Z" fill="#1a1a00"/></svg>
    </span>
  </section>

  <section class="banner micro" aria-label="88 by 31 micro bar">
    <div class="white-panel"></div>
    <div class="photo" role="img" aria-label="Photo of a woman eating a fresh salad"></div>
    <div class="logo logo-green">The Bluvanta Plan</div>
  </section>

</body>
</html>
```